TALBRIDGE VENTORA

I'D LIKE TO REDESIGN MY WEBSITE TO MATCH WITH THE NEW BROCHURE WHICH IS ATTACHED. CONTENT AND LOGOS ARE ATTACHED. PLEASE USE WATCH BRAND LOGOS FROM THE BROCHURE
Coded - Design and coding required
1 page

```html
<!DOCTYPE html>
<html lang="en">
<head>
<meta charset="utf-8">
<title>Talbridge Ventora — Luxury Timepieces</title>
<link rel="stylesheet" href="https://fonts.googleapis.com/css2?family=Marcellus&family=Lato:wght@400;700&family=Montserrat:wght@700&display=swap">
<style>
:root{
  --black:#000;
  --panel:#1a1a1a;
  --footer:#1c1c1c;
  --gold:#c9a437;
  --gold-soft:#b8952e;
  --white:#fff;
  --text:#e6e6e6;
  --grey:#a9a9a9;
  --line:#8a8a8a;
}
*{box-sizing:border-box;margin:0;padding:0}
html,body{width:1200px;height:4134px;overflow:hidden;background:var(--black)}
body{position:relative;font-family:'Lato',sans-serif;color:var(--white)}
.abs{position:absolute}
.serif{font-family:'Marcellus',serif}
.btn{position:absolute;border:2px solid var(--gold);color:var(--gold);font-family:'Marcellus',serif;font-size:15px;display:flex;align-items:center;justify-content:center;letter-spacing:.5px;background:transparent}
.heading{position:absolute;font-family:'Marcellus',serif;color:var(--white);font-weight:400}

/* header */
.site-header{position:absolute;left:0;top:0;width:1200px;height:122px;background:var(--black)}
.brand{position:absolute;display:flex;align-items:center;gap:10px;font-family:'Marcellus',serif;color:var(--gold)}
.brand-mark{width:22px;height:22px;background:var(--gold)}
.nav a{position:absolute;top:52px;font-family:'Marcellus',serif;font-size:15px;color:var(--white);text-decoration:none}
.login{left:985px;top:40px;width:101px;height:42px}

/* hero */
.hero{position:absolute;left:0;top:122px;width:1200px;height:600px;background:#000}
.hero-photo{position:absolute;left:0;top:0;width:680px;height:600px;background:radial-gradient(ellipse at 35% 35%,#4a4a48 0%,#2a2a28 35%,#0d0d0d 70%,#000 100%)}
.hero .welcome{left:688px;top:108px;font-size:29px}
.hero .title{left:688px;top:170px;font-size:62px;line-height:78px;color:var(--gold)}
.hero p{position:absolute;left:688px;top:330px;width:394px;font-size:15px;line-height:26px;text-align:justify;color:var(--text)}
.dots{position:absolute;left:569px;top:548px;display:flex;gap:6px}
.dots span{width:11px;height:11px;border-radius:50%;background:var(--white)}
.dots span.on{background:var(--gold)}

/* about */
.about-panel{position:absolute;left:0;top:722px;width:606px;height:569px;background:#000}
.about-photo{position:absolute;left:606px;top:722px;width:594px;height:569px;background:linear-gradient(160deg,#1c1c1c 0%,#2a2a2a 40%,#8c8c8c 58%,#3a3a3a 72%,#1a1a1a 100%)}
.about-panel p{position:absolute;left:111px;width:426px;font-size:14.5px;line-height:25.7px;text-align:justify;color:var(--text)}

/* invest */
.invest{position:absolute;left:0;top:1291px;width:1200px;height:599px;background:var(--panel)}
.invest-photo{position:absolute;left:152px;top:104px;width:369px;height:418px;border-radius:46% 46% 20% 20%;background:radial-gradient(circle at 50% 38%,#6aa6e0 0%,#2b5a9a 35%,#10203a 62%,#1a1a1a 80%)}
.invest p{position:absolute;left:600px;width:490px;font-size:13px;line-height:21px;color:var(--text)}
.field{position:absolute;border-bottom:1px solid var(--line);height:22px;font-size:12.5px;color:#bdbdbd}
.field svg{position:absolute;right:10px;top:3px}

/* returns */
.returns{position:absolute;left:0;top:1890px;width:1200px;height:622px;background:radial-gradient(ellipse at 50% 45%,#242424 0%,#151515 60%,#0c0c0c 100%)}
.returns p{position:absolute;left:109px;top:189px;width:493px;font-size:15px;line-height:25.7px;text-align:justify;color:var(--text)}
.returns-photo{position:absolute;left:661px;top:159px;width:378px;height:378px;border-radius:50%;border:8px solid var(--gold);background:radial-gradient(circle at 45% 40%,#e8d6a8 0%,#a88f55 40%,#5e4d2a 75%,#2b2416 100%)}

/* brands */
.brands{position:absolute;left:0;top:2512px;width:1200px;height:601px;background:linear-gradient(180deg,#b0b0b0,#a2a2a2)}
.brand-badge{position:absolute;width:102px;height:102px;border-radius:50%;background:var(--white);display:flex;align-items:center;justify-content:center;text-align:center;font-family:'Marcellus',serif;color:#111;font-size:14px;line-height:16px}
.brand-name{position:absolute;font-family:'Marcellus',serif;font-size:20px;color:var(--white)}
.brand-desc{position:absolute;width:300px;font-size:12px;line-height:21px;color:#f1f1f1;text-align:justify}
.view-all{left:537px;top:488px;width:125px;height:43px;background:#111}

/* contact */
.contact{position:absolute;left:0;top:3113px;width:1200px;height:604px;background:#000}
.input{position:absolute;border:1px solid #cfcfcf;border-radius:4px;font-size:14px;color:#e0e0e0;padding:22px 0 0 21px}

/* footer */
.footer{position:absolute;left:0;top:3717px;width:1200px;height:417px;background:var(--footer)}
.foot-h{position:absolute;font-family:'Montserrat',sans-serif;font-weight:700;font-size:17px;color:var(--white)}
.foot-link{position:absolute;left:419px;font-size:13.5px;color:var(--white)}
.foot-item{position:absolute;left:621px;font-size:12.5px;color:var(--white)}
.social{position:absolute;top:233px;width:40px;height:40px;border-radius:50%;background:var(--white);border:2px solid var(--gold)}
.copy{position:absolute;left:0;top:366px;width:1200px;text-align:center;font-family:'Marcellus',serif;font-size:13px;color:var(--white)}
</style>
</head>
<body>

<header class="site-header">
  <div class="brand" style="left:109px;top:48px;font-size:17px"><span class="brand-mark"></span>TALBRIDGE VENTORA</div>
  <nav class="nav">
    <a style="left:396px">HOME</a>
    <a style="left:484px">ABOUT</a>
    <a style="left:577px">INVESTMENTS</a>
    <a style="left:714px">SEARCH WATCHES</a>
    <a style="left:876px">CONTACT</a>
  </nav>
  <div class="btn login">LOG IN</div>
</header>

<section class="hero">
  <div class="hero-photo" role="img" aria-label="Close-up photograph of a dark luxury diver's watch dial"></div>
  <h2 class="heading welcome">WELCOME TO</h2>
  <h1 class="heading title">TALBRIDGE-<br>VENTORA</h1>
  <p>International luxury timepiece supplier. Simply choose a desired product and allow us to source it for you at the best price and with suitable delivery terms.</p>
  <div class="btn" style="left:688px;top:443px;width:127px;height:45px">LEARN MORE</div>
  <div class="dots"><span></span><span class="on"></span><span></span><span></span></div>
</section>

<section class="about-panel">
  <h2 class="heading" style="left:111px;top:85px;font-size:32px">ABOUT US</h2>
  <p style="top:147px">Talbridge Ventora was first founded in 2018, it has been established as the premier resource to buy and sell premium pre-owned watches. With thousands of watches available from brands including Corvane, Aubrey Lenoir, Halden Moreau, Renaud Castell, Veyra, Cavelle and more, plus international locations and clients there's no better place to find a luxury timepiece.</p>
  <p style="top:301px">Outstanding customer service is a mainstay of the Talbridge Ventora ethos. Watch collectors are discerning shoppers, and will accept nothing but the best, which is why customer service has and always will be such an important part of the business.</p>
  <div class="btn" style="left:111px;top:460px;width:128px;height:45px">LEARN MORE</div>
</section>
<div class="about-photo" role="img" aria-label="Macro photograph of a steel watch crown and bracelet"></div>

<section class="invest">
  <div class="invest-photo" role="img" aria-label="Photograph of an ornate skeleton watch with blue sapphire case"></div>
  <h2 class="heading" style="left:600px;top:80px;font-size:32px">WHY INVEST IN WATCHES</h2>
  <p style="top:133px">Previously, investing was focused on traditional investments like stocks, bonds and property.</p>
  <p style="top:194px">One particularly good performer has been luxury watches which have seen buoyant market demand, with investors seeking out largely Swiss-made brands composed of luxurious materials including precious metals like gold and platinum.</p>
  <div class="field" style="left:600px;top:283px;width:221px">Watch brand<svg width="10" height="8" viewBox="0 0 10 8"><path d="M1 2l4 4 4-4" stroke="#ccc" fill="none" stroke-width="1.5"/></svg></div>
  <div class="field" style="left:863px;top:283px;width:225px">Year<svg width="10" height="8" viewBox="0 0 10 8"><path d="M1 2l4 4 4-4" stroke="#ccc" fill="none" stroke-width="1.5"/></svg></div>
  <div class="field" style="left:600px;top:328px;width:488px">Material</div>
  <div class="field" style="left:600px;top:374px;width:221px">Bezel</div>
  <div class="field" style="left:863px;top:374px;width:225px">Strap<svg width="10" height="8" viewBox="0 0 10 8"><path d="M1 2l4 4 4-4" stroke="#ccc" fill="none" stroke-width="1.5"/></svg></div>
  <div class="field" style="left:600px;top:424px;width:488px">Description</div>
  <div class="btn" style="left:600px;top:481px;width:127px;height:45px">LEARN MORE</div>
</section>

<section class="returns" role="region" aria-label="Impressive returns">
  <h2 class="heading" style="left:0;width:1200px;text-align:center;top:82px;font-size:32px">IMPRESSIVE RETURNS</h2>
  <p>A good example of a luxury watch that has seen a substantial increase in value is the steel Halden Moreau Meridian 4820 with the blue dial. When this watch was originally listed in 2006, it retailed at £18,000 (US$30,000); today, it can sell for as much as £190,000 on the pre-owned market which represents a 955% gain. According to the trade press, this watch doubled in price in a short period from US$30,000 to US$65,000. The watch was then discontinued which a saw the price skyrocket to US$90,000 in less than a year. So, we are talking about a 200% gain in less than 12 months which is hard to beat.</p>
  <div class="btn" style="left:109px;top:447px;width:128px;height:45px">LEARN MORE</div>
  <div class="returns-photo" role="img" aria-label="Photograph of a gold watch movement seen through a caseback"></div>
</section>

<section class="brands">
  <h2 class="heading" style="left:0;width:1200px;text-align:center;top:62px;font-size:28px">BEST WATCH BRAND TO INVEST IN</h2>

  <div class="brand-badge" style="left:148px;top:159px">CORVANE</div>
  <div class="brand-name" style="left:266px;top:148px">CORVANE</div>
  <div class="brand-desc" style="left:266px;top:188px">Without a doubt, Corvane is seen to be one of the best investment watch brands. Corvane watches can be great investments but choose wisely as certain designs are a lot more valuable than others.</div>

  <div class="brand-badge" style="left:636px;top:159px;font-size:12px">HALDEN<br>MOREAU</div>
  <div class="brand-name" style="left:754px;top:148px">HALDEN MOREAU</div>
  <div class="brand-desc" style="left:754px;top:188px">Without a doubt, Halden Moreau is seen to be one of the best investment watch brands. Its watches can be great investments but choose wisely as certain designs are a lot more valuable than others.</div>

  <div class="brand-badge" style="left:148px;top:324px">VEYRA</div>
  <div class="brand-name" style="left:266px;top:314px">VEYRA</div>
  <div class="brand-desc" style="left:266px;top:353px">Respected for making a number of the best watches available today, Veyra has set more precision records than others and is synonymous with space travel which results in its watches being in high demand in the pre-owned market.</div>

  <div class="brand-badge" style="left:636px;top:324px">BRISANT</div>
  <div class="brand-name" style="left:754px;top:314px">BRISANT</div>
  <div class="brand-desc" style="left:754px;top:353px;width:300px">This brand is seen as a cut price Corvane. The story is that Edmund Kessler, the creator of Corvane, designed Brisant to be able to sell watches at a more affordable price.</div>

  <div class="btn view-all">VIEW ALL</div>
</section>

<section class="contact">
  <h2 class="heading" style="left:0;width:1200px;text-align:center;top:84px;font-size:28px">CONTACT US</h2>
  <div class="input" style="left:204px;top:148px;width:383px;height:64px">First Name</div>
  <div class="input" style="left:611px;top:148px;width:384px;height:64px">Last Name</div>
  <div class="input" style="left:204px;top:233px;width:383px;height:63px">Your Email</div>
  <div class="input" style="left:611px;top:233px;width:384px;height:63px">Phone</div>
  <div class="input" style="left:204px;top:317px;width:788px;height:128px;padding-top:20px">Message</div>
  <div class="btn" style="left:537px;top:472px;width:125px;height:45px">SUBMIT</div>
</section>

<footer class="footer">
  <div class="brand" style="left:109px;top:162px;font-size:20px"><span class="brand-mark"></span>TALBRIDGE VENTORA</div>

  <div class="foot-h" style="left:419px;top:103px">QUICK LINKS</div>
  <div class="foot-link" style="top:152px">Home</div>
  <div class="foot-link" style="top:178px">About</div>
  <div class="foot-link" style="top:204px">Investments</div>
  <div class="foot-link" style="top:229px">Search Watches</div>
  <div class="foot-link" style="top:255px">Contact</div>

  <div class="foot-h" style="left:590px;top:103px">CONTACT US</div>
  <svg class="abs" style="left:591px;top:160px" width="16" height="20" viewBox="0 0 16 20"><path d="M8 0C3.6 0 0 3.5 0 7.8 0 13.5 8 20 8 20s8-6.5 8-12.2C16 3.5 12.4 0 8 0zm0 11a3.2 3.2 0 110-6.4A3.2 3.2 0 018 11z" fill="#fff"/></svg>
  <div class="foot-item" style="top:163px">TBC</div>
  <svg class="abs" style="left:591px;top:199px" width="17" height="17" viewBox="0 0 24 24"><path d="M6.6 10.8a15.1 15.1 0 006.6 6.6l2.2-2.2a1 1 0 011-.25 11.4 11.4 0 003.6.57 1 1 0 011 1V20a1 1 0 01-1 1A17 17 0 013 4a1 1 0 011-1h3.5a1 1 0 011 1c0 1.25.2 2.45.57 3.6a1 1 0 01-.25 1z" fill="#fff"/></svg>
  <div class="foot-item" style="top:201px">0161 555 0192</div>
  <svg class="abs" style="left:591px;top:238px" width="18" height="13" viewBox="0 0 18 13"><rect width="18" height="13" rx="1" fill="#fff"/><path d="M1 1l8 6 8-6" stroke="#1c1c1c" stroke-width="1.5" fill="none"/></svg>
  <div class="foot-item" style="top:236px">sales@talbridge-ventora.example</div>

  <div class="foot-h" style="left:865px;top:103px">NEWSLETTER</div>
  <div class="abs" style="left:865px;top:154px;width:170px;height:40px;background:#fff;border-radius:5px 0 0 5px;font-size:14px;color:#888;padding:11px 0 0 13px">Enter email</div>
  <div class="abs" style="left:1035px;top:154px;width:54px;height:40px;background:var(--gold);border-radius:0 5px 5px 0;display:flex;align-items:center;justify-content:center">
    <svg width="16" height="12" viewBox="0 0 18 13"><rect width="18" height="13" rx="1" fill="#fff"/><path d="M1 1l8 6 8-6" stroke="#c9a437" stroke-width="1.5" fill="none"/></svg>
  </div>
  <div class="social" style="left:881px" role="img" aria-label="Social profile link"></div>
  <div class="social" style="left:936px" role="img" aria-label="Social profile link"></div>
  <div class="social" style="left:990px" role="img" aria-label="Social profile link"></div>
  <div class="social" style="left:1045px" role="img" aria-label="Social profile link"></div>

  <div class="abs" style="left:109px;top:322px;width:982px;height:1px;background:#3a3a3a"></div>
  <div class="copy">©Copyrights 2022 Talbridge-Ventora &nbsp;| &nbsp;&nbsp;All Rights Reserved</div>
</footer>

</body>
</html>
```